Building and Facilities Management brochure

Please refer to attached PDF, page by page with information about the brief.
SOPHISTICATED, BOLD, PROFESSIONAL BROCHURE to market our company in business meetings to Builders, Owners of buildings, Strata Committees etc.

The final design should portray quality, service, integrity,
Clear Communication

Attached is:
- pdf with details of basic layout options and wording and most of the information about the brief.
- Logo options to use
- Business card designs to understand what design we have previously had.
- Word document of the pdf if that helps to copy the information.

Target Market(s)

Professionals. Builders/developer, Strata Owners, and Building owners who want a high level of service and management of their building

Industry/Entity Type

It Company

Requirements
Must have
• - Logo
• - Contact details
• - Use of the colour in the design which has been specified.
• - Images/s of building/s
• - Use the phrase "Quality Service with Integrity"
Nice to have
• - as much of the wording as possible from the document which was uploaded, that will fit and work with the design
Should not have
• Excessive colour or variances as it needs to stay clear, bold and sophisticated.
• Too much on the page, clarity is key for clear communication without trying to clutter too much on the page.

```html
<!DOCTYPE html>
<html lang="en">
<head>
<meta charset="utf-8">
<title>Harbourline Property Services – Brochure</title>
<link href="https://fonts.googleapis.com/css2?family=Comfortaa:wght@400;700&family=Josefin+Sans:wght@300;400&family=Montserrat:wght@400;500;600;700&display=swap" rel="stylesheet">
<style>
  :root{
    --bg:#d9dadc;
    --blue:#1d8fd9;
    --blue-deep:#0f5fa8;
    --blue-light:#6cc0f0;
    --night:#0d2a55;
    --ink:#3a3f47;
    --muted:#7b828c;
    --paper:#ffffff;
  }
  *{box-sizing:border-box;margin:0;padding:0}
  html,body{width:960px;height:1200px;overflow:hidden;background:var(--bg)}
  body{position:relative;font-family:'Montserrat',sans-serif;color:var(--ink)}
  .spread{position:absolute;left:90px;width:780px;height:552px;display:flex;box-shadow:0 8px 24px rgba(0,0,0,.18)}
  .spread--outer{top:32px}
  .spread--inner{top:616px}
  .page{position:relative;width:390px;height:552px;overflow:hidden;background:var(--paper)}
  .photo{position:absolute}

  /* brand name */
  .brand{display:flex;align-items:center;gap:8px;font-family:'Montserrat',sans-serif;font-weight:600;letter-spacing:.08em;text-transform:uppercase}
  .brand__mark{width:16px;height:16px;flex:none}
  .brand__name{font-size:13px;line-height:1.25}

  /* back cover */
  .back{background:var(--blue)}
  .back .photo{left:0;top:0;width:390px;height:420px;background:linear-gradient(180deg,#2aa2ea 0%,#1b86d2 55%,#1672c0 100%)}
  .faint-words{position:absolute;font-family:'Josefin Sans',sans-serif;font-weight:300;text-transform:uppercase;color:rgba(255,255,255,.16);line-height:1}
  .back .faint-words{left:10px;top:38px;font-size:42px;letter-spacing:.04em}
  .back .brand{position:absolute;left:0;right:0;top:218px;justify-content:center;color:#fff}
  .back .brand__mark{background:#fff}
  .back__contact{position:absolute;left:0;top:420px;width:390px;height:132px;background:var(--paper);padding:22px 28px}
  .contact__title{font-family:'Comfortaa',sans-serif;font-size:17px;color:var(--blue);margin-bottom:12px}
  .contact__line{font-size:9px;font-weight:600;color:var(--ink);line-height:1.7}

  /* front cover */
  .front .photo{left:0;top:0;width:390px;height:350px;background:linear-gradient(180deg,#7fcdf5 0%,#3a9ee0 35%,#1a5da8 62%,#0e3270 80%,#2a6fba 100%)}
  .tagline{position:absolute;left:30px;top:40px;width:262px;padding:12px 14px;border:1.5px solid rgba(255,255,255,.85);font-family:'Josefin Sans',sans-serif;color:#fff;text-align:center;text-transform:uppercase;line-height:1.15}
  .tagline__big{font-size:22px}
  .tagline__small{font-size:14px}
  .front .brand{position:absolute;right:26px;top:425px;color:var(--blue)}
  .front .brand__mark{background:var(--blue)}
  .front__web{position:absolute;left:24px;top:482px;font-size:7px;color:var(--muted);letter-spacing:.02em}

  /* inner shared */
  .section-title{font-family:'Comfortaa',sans-serif;color:var(--blue);font-weight:400}
  .copy{font-size:8px;line-height:1.6;color:var(--ink)}
  .copy b{font-weight:700;text-transform:uppercase;color:#2c3138}

  /* inner left */
  .vision .photo{left:0;top:0;width:390px;height:150px;background:linear-gradient(180deg,#2d66b8 0%,#17407f 55%,var(--night) 100%)}
  .vision__title{position:absolute;left:26px;top:108px;font-family:'Comfortaa',sans-serif;font-size:26px;color:#fff}
  .vision__text{position:absolute;left:26px;top:166px;width:340px}
  .vision__text p+p{margin-top:10px}
  .aspects__title{position:absolute;left:26px;top:318px;font-size:25px}
  .aspects__col{position:absolute;width:160px}
  .aspects__col p+p{margin-top:9px}
  .aspects__col--left{left:26px;top:360px}
  .aspects__col--right{left:208px;top:318px;width:160px}
  .handshake{left:208px;top:446px;width:160px;height:82px;background:linear-gradient(135deg,#1d2f52 0%,#3a5a8e 50%,#0f1b35 100%)}

  /* inner right */
  .services .photo--band{left:0;top:0;width:390px;height:70px;background:linear-gradient(180deg,var(--blue) 0%,#6cc0f0 60%,#fff 100%)}
  .services .faint-words{right:14px;top:6px;font-size:20px;text-align:right;color:rgba(255,255,255,.35)}
  .services__title{position:absolute;left:24px;top:78px;font-size:22px}
  .sub-title{font-family:'Montserrat',sans-serif;font-weight:700;font-size:10px;color:#2c3138;letter-spacing:.03em}
  .core__head{position:absolute;left:24px;top:110px;width:340px}
  .core__head .copy{font-size:6.5px;line-height:1.4;margin-top:2px}
  .core__grid{position:absolute;left:24px;top:148px;display:flex;gap:6px}
  .tile{position:relative;width:111px;height:74px;overflow:hidden}
  .tile__img{position:absolute;inset:0}
  .tile__img--building{background:linear-gradient(160deg,#bfe3fb 0%,#3a8fd6 60%,#1c5aa0 100%)}
  .tile__img--facilities{background:linear-gradient(160deg,#f2f4f6 0%,#cfd6de 60%,#9aa6b3 100%)}
  .tile__img--caretaker{background:linear-gradient(160deg,#eef1f3 0%,#d5dadf 55%,#aeb8c2 100%)}
  .tile__cap{position:absolute;left:0;right:0;bottom:0;height:14px;background:var(--blue);color:#fff;font-size:6.5px;line-height:14px;text-align:center}
  .value__head{position:absolute;left:24px;top:240px;width:200px}
  .value__head .copy{font-size:7px;line-height:1.55;margin-top:6px}
  .checklist{position:absolute;left:244px;top:240px;list-style:none}
  .checklist li{display:flex;align-items:center;gap:6px;font-size:7.5px;color:var(--ink);margin-bottom:6px}
  .checklist svg{width:9px;height:9px;flex:none}
  .collage{left:24px;top:356px;width:204px;height:120px;background:linear-gradient(135deg,#8a5a3a 0%,#c9d3dc 35%,#e8ecef 55%,#3f6ea8 80%,#d9dde1 100%)}
  .cta{position:absolute;left:244px;top:372px;width:128px;font-size:7.5px;font-weight:700;line-height:1.5;color:var(--blue)}
</style>
</head>
<body>

<section class="spread spread--outer">
  <article class="page back">
    <div class="photo" role="img" aria-label="Blue-toned city skyline reflected in water"></div>
    <div class="faint-words">Quality<br>Service<br>Integrity</div>
    <div class="brand">
      <span class="brand__mark"></span>
      <span class="brand__name">Harbourline<br>Property Services</span>
    </div>
    <div class="back__contact">
      <h3 class="contact__title">Contact Information</h3>
      <p class="contact__line">info@harbourlineproperty.com.au &nbsp;|&nbsp; www.harbourlineproperty.com.au</p>
      <p class="contact__line">Bayside City and surrounding suburbs through to the Southern Coast</p>
    </div>
  </article>

  <article class="page front">
    <div class="photo" role="img" aria-label="City skyline at dusk reflected in a river"></div>
    <div class="tagline">
      <span class="tagline__big">Quality</span> <span class="tagline__small">Service</span><br>
      <span class="tagline__small">with</span> <span class="tagline__big">Integrity</span>
    </div>
    <div class="brand">
      <span class="brand__mark"></span>
      <span class="brand__name">Harbourline<br>Property Services</span>
    </div>
    <p class="front__web">www.harbourlineproperty.com.au</p>
  </article>
</section>

<section class="spread spread--inner">
  <article class="page vision">
    <div class="photo" role="img" aria-label="City skyline at night"></div>
    <h2 class="vision__title">Vision</h2>
    <div class="vision__text copy">
      <p>At HPS, our aim is to provide complete solutions for Building and Facilities Owners and Strata Corporations in the management of their assets. With the understanding that each property has different needs and requirements, our focus is to work with clients to tailor solutions best suited to their specific needs.</p>
      <p>Our aim is to ensure the Building and Facilities are managed to the highest standards using the latest technological management solutions to efficiently and effectively control all aspects of the building. With a keen focus on controlling costs to ensure funds are spent cost-effectively, through improved operations and management of all aspects of the building.</p>
    </div>
    <h2 class="aspects__title section-title">Key Aspects</h2>
    <div class="aspects__col aspects__col--left copy">
      <p><b>Compliance</b> with relevant industry acts and regulations</p>
      <p><b>OH&amp;S</b> to ensure the building and aspects are controlled safely and the risk of all contractors and owners is reduced and managed.</p>
      <p><b>Preventative Maintenance</b> to ensure assets are professionally maintained to ensure the best reliability and longevity of each asset.</p>
      <p><b>Reactive Maintenance</b> to ensure any issues that arise are resolved and handled as efficiently as possible.</p>
    </div>
    <div class="aspects__col aspects__col--right copy">
      <p><b>Communication</b> to ensure the Committee and Owners have clear and concise information and knowledge of the aspects of their building and assets.</p>
      <p><b>Relationships</b> are a top priority as they are paramount for effective management with Owners, Residents, Developers and Strata Managers.</p>
    </div>
    <div class="photo handshake" role="img" aria-label="Business handshake"></div>
  </article>

  <article class="page services">
    <div class="photo photo--band" role="img" aria-label="Faded blue city skyline"></div>
    <div class="faint-words">Quality<br>Service<br>Integrity</div>
    <h2 class="services__title section-title">Services</h2>
    <div class="core__head">
      <h3 class="sub-title">CORE SERVICES</h3>
      <p class="copy">These are the core focus of the business to provide the highest standard in Building and Facilities Management.</p>
    </div>
    <div class="core__grid">
      <figure class="tile"><div class="tile__img tile__img--building" role="img" aria-label="Glass office tower"></div><figcaption class="tile__cap">Building Management</figcaption></figure>
      <figure class="tile"><div class="tile__img tile__img--facilities" role="img" aria-label="Modern office interior"></div><figcaption class="tile__cap">Facilities Management</figcaption></figure>
      <figure class="tile"><div class="tile__img tile__img--caretaker" role="img" aria-label="Clean building lobby"></div><figcaption class="tile__cap">Caretaker</figcaption></figure>
    </div>
    <div class="value__head">
      <h3 class="sub-title">VALUE ADDED SERVICES</h3>
      <p class="copy">In addition to the Core Service we are proud to offer these Value Added services to complement the management of the Building, or offer as stand-alone services to assist owners with the management of their Building and Assets.</p>
    </div>
    <ul class="checklist">
      <li><svg viewBox="0 0 10 10"><rect x=".5" y=".5" width="9" height="9" fill="none" stroke="#1d8fd9"/><path d="M2.2 5.2l2 2 3.8-4.4" fill="none" stroke="#1d8fd9" stroke-width="1.3"/></svg>Concierge</li>
      <li><svg viewBox="0 0 10 10"><rect x=".5" y=".5" width="9" height="9" fill="none" stroke="#1d8fd9"/><path d="M2.2 5.2l2 2 3.8-4.4" fill="none" stroke="#1d8fd9" stroke-width="1.3"/></svg>Cleaning</li>
      <li><svg viewBox="0 0 10 10"><rect x=".5" y=".5" width="9" height="9" fill="none" stroke="#1d8fd9"/><path d="M2.2 5.2l2 2 3.8-4.4" fill="none" stroke="#1d8fd9" stroke-width="1.3"/></svg>Project Management</li>
      <li><svg viewBox="0 0 10 10"><rect x=".5" y=".5" width="9" height="9" fill="none" stroke="#1d8fd9"/><path d="M2.2 5.2l2 2 3.8-4.4" fill="none" stroke="#1d8fd9" stroke-width="1.3"/></svg>Electrical</li>
      <li><svg viewBox="0 0 10 10"><rect x=".5" y=".5" width="9" height="9" fill="none" stroke="#1d8fd9"/><path d="M2.2 5.2l2 2 3.8-4.4" fill="none" stroke="#1d8fd9" stroke-width="1.3"/></svg>Handyman</li>
      <li><svg viewBox="0 0 10 10"><rect x=".5" y=".5" width="9" height="9" fill="none" stroke="#1d8fd9"/><path d="M2.2 5.2l2 2 3.8-4.4" fill="none" stroke="#1d8fd9" stroke-width="1.3"/></svg>New site setup</li>
      <li><svg viewBox="0 0 10 10"><rect x=".5" y=".5" width="9" height="9" fill="none" stroke="#1d8fd9"/><path d="M2.2 5.2l2 2 3.8-4.4" fill="none" stroke="#1d8fd9" stroke-width="1.3"/></svg>Building defect management</li>
    </ul>
    <div class="photo collage" role="img" aria-label="Collage of service photos: concierge, cleaning, meetings, electrical work, trades and floor plans"></div>
    <p class="cta">Please feel free to contact us to enquire about any of the above services, either individually or as multiple services to ensure the best value can be provided for your requirements.</p>
  </article>
</section>

</body>
</html>
```